Attorney Business Card

I need a business card that looks professional yet modern. I am an Attorney. , I need a professional yet modern business card for my law practice. My logo and information have been uploaded. , I need a business card that looks professional yet modern. I am an Attorney. , I need a professional yet modern business card for my law practice. My logo and information have been uploaded.

Industry/Entity Type

Business

Requirements
Must have
• My logo which has been uploaded , my logo , My logo which has been uploaded , my logo

```html
<!DOCTYPE html>
<html lang="en">
<head>
<meta charset="utf-8">
<title>Mercer Law Firm – Business Card</title>
<link rel="stylesheet" href="https://fonts.googleapis.com/css2?family=Mulish:wght@400;500;600&display=swap">
<style>
  :root {
    --backdrop: #2b2b2c;
    --card-white: #f4f4f2;
    --navy: #244f78;
    --ink: #1f1f22;
    --paper-text: #f2f4f7;
  }
  html, body {
    margin: 0;
    padding: 0;
    width: 1200px;
    height: 900px;
    overflow: hidden;
    background: var(--backdrop);
    font-family: "Mulish", "Helvetica Neue", Arial, sans-serif;
  }
  .canvas {
    position: relative;
    width: 1200px;
    height: 900px;
  }
  .card {
    position: absolute;
    left: 355px;
    width: 486px;
    height: 270px;
    box-sizing: border-box;
  }
  .card--front {
    top: 158px;
    background: var(--card-white);
    color: var(--ink);
  }
  .card--back {
    top: 467px;
    background: var(--navy);
    color: var(--paper-text);
  }

  /* Front */
  .person {
    position: absolute;
    left: 34px;
    top: 48px;
  }
  .person__name {
    margin: 0;
    font-size: 15px;
    font-weight: 500;
    letter-spacing: 0.2px;
  }
  .person__line {
    margin: 4px 0 0;
    font-size: 12.5px;
  }
  .person__role {
    color: var(--navy);
    margin-left: 5px;
  }
  .info-block {
    position: absolute;
    left: 34px;
    padding-left: 10px;
    border-left: 3px solid var(--navy);
    font-size: 12.5px;
    line-height: 16px;
  }
  .info-block--phones { top: 106px; }
  .info-block--address { top: 176px; }
  .info-block p { margin: 0; }
  .info-block__label {
    display: inline-block;
    width: 14px;
    color: var(--navy);
    font-weight: 600;
  }

  .firm-mark {
    position: absolute;
    display: flex;
    align-items: center;
    gap: 8px;
    font-weight: 600;
    letter-spacing: 1.5px;
    text-transform: uppercase;
    white-space: nowrap;
  }
  .firm-mark__dot {
    flex: none;
    border-radius: 50%;
  }
  .card--front .firm-mark {
    left: 290px;
    top: 124px;
    font-size: 16px;
    color: var(--navy);
  }
  .card--front .firm-mark__dot {
    width: 12px;
    height: 12px;
    background: var(--navy);
  }

  /* Back */
  .card--back .firm-mark {
    left: 50%;
    top: 120px;
    transform: translateX(-50%);
    font-size: 22px;
    color: var(--paper-text);
  }
  .card--back .firm-mark__dot {
    width: 16px;
    height: 16px;
    background: var(--paper-text);
  }
  .website {
    position: absolute;
    left: 0;
    right: 0;
    top: 234px;
    margin: 0;
    text-align: center;
    font-size: 12.5px;
    font-weight: 600;
    letter-spacing: 1.6px;
  }
</style>
</head>
<body>
<main class="canvas">
  <section class="card card--front" aria-label="Business card front">
    <div class="person">
      <h1 class="person__name">Daniel Mercer, ESQ.</h1>
      <p class="person__line">daniel@mercerlegal.com<span class="person__role">Attorney at law</span></p>
    </div>
    <div class="info-block info-block--phones">
      <p><span class="info-block__label">T</span> 310.555.0142</p>
      <p><span class="info-block__label">F</span> 310.555.0143</p>
      <p><span class="info-block__label">M</span> 310.555.0178</p>
    </div>
    <div class="info-block info-block--address">
      <p>2180 Harbor Ave.</p>
      <p>Penthouse</p>
      <p>Westfield, CA 90417</p>
    </div>
    <div class="firm-mark">
      <span class="firm-mark__dot"></span>
      <span class="firm-mark__name">Mercer Law Firm</span>
    </div>
  </section>

  <section class="card card--back" aria-label="Business card back">
    <div class="firm-mark">
      <span class="firm-mark__dot"></span>
      <span class="firm-mark__name">Mercer Law Firm</span>
    </div>
    <p class="website">www.mercerlegal.com</p>
  </section>
</main>
</body>
</html>
```